Systems and Technology Consultants - Website

Design & Build a website for a new company which operates in the Systems and Technology space for Transportation, Government and Commercial sectors.

Overall design should be minimalist in nature.
Should also have a feed that provides news and event updates on the main page.
Logo has already been awarded and should be incorporated into the site.

We like the overall layout, functionality and simplicity of the below sites. Submitted designs could be similar to or a combination of the aspects on these sites, or perhaps a whole different concept - we are open to new ideas.
Vortrane.com
Merp.it

Update 1 Dated 27 May 2014

All I am moving away from the Merp.it website and would like it to be more aligned with Vortrane.com not only in layout but in functionality. I will be extending the deadline of this design brief for two weeks to incorporate additional requirements and will add addtional funding to the project.

Apologies for not having more information available to provide but with so many submissions its getting confusing.

Thanks Dermot
Updates

Please note that the brief has been updated and the deadline has been extended.

Important: We will need two language versions of the website, English and Arabic; the website is hosted on HostPeak

Hello All, Thank you for your submissions. We have narrowed it down to the final 6 designers and I just wanted to take a moment and provide a bit of feedback regarding the concepts that we like and the modifications we are looking for. First, let me mention some of the design functions we like. - At the top of the homepage we really like the "region" or "language" tab so that the website can be viewed in both English and Arabic. - We like the homepage to have clear color variation so that the different sections of the homepage are distinct. Additionally, we like the bottom portion of the homepage to be in red. We feel that draws attention to our contact information. Again, we would like the colors to integrate black, gray-scale, red, etc. - Having a search tab at the top of the home page, or integrated into the main image, so that the site is easy to navigate. - We especially like the main image to have the scrolling tabs at the bottom so it is easy to browse the services offered (Consultancy, Solutions Architecture, Masters Systems Integration, Independent Design Review). - In regards to the services offered tab we really like the idea that a few people presented that have the outside of our logo with an icon in the middle of consultancy, solutions, etc., etc. Secondly, as mentioned in our brief we really enjoy the design of vortrane site. Specially, we enjoy the strong iconic images they use, the way the tabs at the top scroll easily, and contact us page that generates an email. Lastly, I've included some photos of the concept we have been working on. What we are trying to demonstrate is how our company offers a range of services that are essentially linked together. We provide individual services that when combined present the full service package. We would like this concept to be integrated into the over concept of our website. Please feel free to ask for clarification of any of the above points or contact us if you have any additional questions. We appreciate all of your hard work and are very excited to see the updated designs. Best, Miriam Dowbrook Plenvaro Senior Program Manager miriam.dowbrook@plenvaro-mail.com

Industry/Entity Type

Government

Font styles to use
Serif
Sans Serif

Requirements
Must have
• Must work on/adapt to various/mobile devices (responsive)
Must be simple and straightforward
Colors should be in line/matching with logo
2 language versions: English and Arabic (no Thai)
Services should be the first group/row of items after/below the main image
Note: the website will be hosted by hostpeak
Nice to have
• Submit feedback form
What's New section
The banner at the bottom of the site should not be too large; we would like a narrow one more
It would be nice if the header/top banner (with Home, About, etc. tabs) could stay in place as you scroll down (like Vortrane and Chatterly)
We will likely only use one image with a Company slogan on the Home page rather than a carousel of images to rotate through
Should not have
• This is the existing website: http://www.plenvaro-example.org
We do not like the animation, the way the banner icons/titles bounce
Not simple enough, we don't like the functionality or how pages load so slowly
We do not like the logo centered - it should be at the left
The banner and its tabs should not be towards the right, we would like them to be centered, to go all the way across and to be below the logo

```html
<!DOCTYPE html>
<html lang="en">
<head>
<meta charset="utf-8">
<title>Plenvaro International</title>
<link href="https://fonts.googleapis.com/css2?family=Oxygen:wght@300;400;700&display=swap" rel="stylesheet">
<style>
:root{
  --red:#e3141b;
  --ink:#1d1d1d;
  --text:#555;
  --muted:#6d6d6d;
  --line:#dcdcdc;
  --blue-deep:#0d34a6;
  --blue-mid:#3c6fd1;
  --blue-light:#a9c4ec;
  --footer-bg:#f4f4f4;
}
*{margin:0;padding:0;box-sizing:border-box}
html,body{width:951px;height:1200px;overflow:hidden;background:#fff}
body{font-family:"Oxygen",Arial,sans-serif;color:var(--ink);position:relative}

.site-header{position:absolute;left:0;top:0;width:951px;height:86px;background:linear-gradient(#fff,#f7f7f7)}
.brand{position:absolute;left:80px;top:30px;display:flex;align-items:center;gap:9px}
.brand-mark{width:14px;height:14px;background:var(--red)}
.brand-name{font-size:17px;font-weight:700;color:var(--red);letter-spacing:2px;text-transform:uppercase}
.main-nav{position:absolute;top:41px;left:393px;display:flex;gap:0}
.main-nav a{font-size:14.5px;color:var(--ink);text-decoration:none;margin-right:37px}

.hero{position:absolute;left:0;top:86px;width:951px;height:372px;
  background:linear-gradient(100deg,var(--blue-deep) 0%,#1f4fbf 38%,var(--blue-mid) 58%,var(--blue-light) 85%,#dfe8f6 100%)}
.hero-copy{position:absolute;left:86px;top:110px;color:#fff}
.hero-title{font-size:29px;font-weight:700;line-height:1.1}
.hero-sub{font-size:20px;font-weight:300;margin-top:5px}
.hero-text{font-size:10px;line-height:17px;color:#b9c8ec;margin-top:10px}
.hero-dots{display:flex;gap:4px;margin-top:13px}
.hero-dots span{width:10px;height:10px;border-radius:50%;background:#fff}

.services{position:absolute;left:79px;top:471px;width:797px;height:193px;display:flex}
.service-card{flex:1;border:1px solid var(--line);border-radius:3px;background:linear-gradient(#fff 70%,#f5f5f5);padding:11px 12px 0}
.service-photo{height:97px}
.service-card h3{font-size:16px;font-weight:400;color:var(--red);margin:10px 0 3px 2px}
.service-card p{font-size:10px;line-height:16px;color:var(--muted);margin-left:2px}

.welcome{position:absolute;left:78px;top:706px;width:520px}
.welcome h2,.partners h2{font-size:23px;font-weight:300;color:var(--ink)}
.welcome p{font-size:9.6px;line-height:17px;color:var(--text);margin:9px 0 0 2px}

.partners{position:absolute;left:636px;top:707px;width:230px}
.partner-grid{display:grid;grid-template-columns:repeat(3,58px);column-gap:25px;row-gap:22px;margin-top:15px}
.partner-badge{height:24px;border-radius:4px;background:#d9dce3}

.site-footer{position:absolute;left:0;top:926px;width:951px;height:222px;background:linear-gradient(#ececec,var(--footer-bg) 20%,#f7f7f7);border-top:1px solid #ddd}
.footer-col{position:absolute;top:34px}
.footer-col h4{font-size:14px;font-weight:400;text-transform:uppercase;color:var(--ink);margin-bottom:8px}
.footer-col li{list-style:none;font-size:10.5px;line-height:19.5px;color:#333;padding-left:1px}

.legal{position:absolute;left:0;top:1148px;width:951px;height:52px;border-top:1px solid var(--line);background:#fff}
.legal p{position:absolute;left:77px;top:19px;font-size:10px;color:#333}
.social{position:absolute;left:775px;top:16px;display:flex;gap:6px}
.social span{width:17px;height:17px;border-radius:2px}
</style>
</head>
<body>

<header class="site-header">
  <div class="brand"><span class="brand-mark"></span><span class="brand-name">Plenvaro International</span></div>
  <nav class="main-nav">
    <a href="#">Home</a><a href="#">About Us</a><a href="#">Services</a><a href="#">Business Unit</a><a href="#">Contact Us</a>
  </nav>
</header>

<section class="hero" role="img" aria-label="Low-angle view of glass high-rise buildings under construction with tower cranes against a blue sky">
  <div class="hero-copy">
    <h1 class="hero-title">Construction &amp; Engineering</h1>
    <p class="hero-sub">Maecenas justo velit placerat</p>
    <p class="hero-text">Phasellus felis dolor scelerisque a tempus eget lobortis id libero<br>Aliquam nec erat at purus cursus interdum Vestibul</p>
    <div class="hero-dots"><span></span><span></span><span></span><span></span></div>
  </div>
</section>

<section class="services">
  <article class="service-card">
    <div class="service-photo" role="img" aria-label="Hands reviewing charts on a clipboard beside a keyboard" style="background:linear-gradient(135deg,#e9ecef,#b9c3cf)"></div>
    <h3>Consulting</h3><p>Aliquam nec erat at purus cursus interdum Vestibulum ligula</p>
  </article>
  <article class="service-card">
    <div class="service-photo" role="img" aria-label="Engineers discussing plans at a desk in an office" style="background:linear-gradient(135deg,#cfd6dc,#8e9aa6)"></div>
    <h3>Engineering</h3><p>Aliquam nec erat at purus cursus interdum Vestibulum ligula</p>
  </article>
  <article class="service-card">
    <div class="service-photo" role="img" aria-label="Yellow hard hat held beside a construction tool belt" style="background:linear-gradient(135deg,#9aa3ab,#e8c23a 55%,#6c7276)"></div>
    <h3>Construction</h3><p>Aliquam nec erat at purus cursus interdum Vestibulum ligula</p>
  </article>
  <article class="service-card">
    <div class="service-photo" role="img" aria-label="Technician in a hard hat working on industrial pipework" style="background:linear-gradient(135deg,#6b6357,#c79a3c 60%,#4c4d52)"></div>
    <h3>Maintenance</h3><p>Aliquam nec erat at purus cursus interdum Vestibulum ligula</p>
  </article>
</section>

<section class="welcome">
  <h2>Welcome to Plenvaro Website</h2>
  <p>Plenvaro specializes in delivering quality professional services and technical projects that support larger business goals.&nbsp; systems are tools that support a greater business function and need. we understand that most technical projects are conceptualized to support a larger vision with actual business goals in mind and ensure that all of our professional and certified expertise is included in our professional services to meet those goals.</p>
  <p>plenvaro recognizes the middle east and greater asia regions are economic growth markets with developing infrastructure projects requiring specialist systems and technical expertise.&nbsp; accordingly, plenvaro has evolved its presence in the regions to meet client demands and expectations.</p>
</section>

<aside class="partners">
  <h2>Partners</h2>
  <div class="partner-grid">
    <span class="partner-badge"></span><span class="partner-badge"></span><span class="partner-badge"></span>
    <span class="partner-badge"></span><span class="partner-badge"></span><span class="partner-badge"></span>
    <span class="partner-badge"></span><span class="partner-badge"></span><span class="partner-badge"></span>
  </div>
</aside>

<footer class="site-footer">
  <div class="footer-col" style="left:80px"><h4>Company</h4><ul><li>About Us</li><li>Services</li><li>Solutions</li><li>Case Studies</li><li>Awards</li></ul></div>
  <div class="footer-col" style="left:235px"><h4>Features</h4><ul><li>Sed porta</li><li>Suspendisse quam</li><li>Leo molestie</li><li>Sed luctus quis</li><li>Tempor cursus</li></ul></div>
  <div class="footer-col" style="left:399px"><h4>Services</h4><ul><li>Phasellus felis dolor</li><li>Scelerisque tempus</li><li>Eget lobortis</li><li>Libero Aliquam</li></ul></div>
  <div class="footer-col" style="left:563px"><h4>Support</h4><ul><li>Sed porta</li><li>Suspendisse quam</li><li>Leo molestie</li><li>Sed luctus quis</li></ul></div>
  <div class="footer-col" style="left:711px"><h4>Contact</h4><ul><li>48 Harlow Quay, Suite 210</li><li>Brentmoor, Ostland 40217</li><li>Tel: +00 (0)1555 302100</li><li>Fax: +00 (0)1555 302155</li><li>sales@plenvaro-mail.com</li></ul></div>
</footer>

<div class="legal">
  <p>© 2014 Company Name.&nbsp; All right reserved.&nbsp; Term of Use</p>
  <div class="social">
    <span style="background:#3b5a9a"></span><span style="background:#3fb2e2"></span><span style="background:#1f6fa8"></span><span style="background:#f28a1c"></span>
  </div>
</div>

</body>
</html>
```